Sign Shop website

We need a web design for a sign company called Quanta Signs that builds signs for shops such as A Frames, Banners, Tennet Boards, Shop front windows etc...

The existing site is avaliable at www.quantasigns-demo.com.au

We will need to have a fresh makeover. The new site must have the following:

Photo Galleries (broken down into sections)
Store Locations (currently there are 4 stores)
Online quote form
List of services
About Us Page

We just need to front page designed in photoshop (the inner page is not necessary) We have a team that can code the site up.

The website should have the exact logo. Any person who alters the logo, design will be elimated.

No Twitter, RSS, LinkedIn icons

The main colours are yellow, black, blue, red

Target Market(s)

Any business

Industry/Entity Type

It Company

Requirements
Must have
• jQuery slider banner
Should not have
• Alter the logo in any way

```html
<!DOCTYPE html>
<html lang="en">
<head>
<meta charset="utf-8">
<title>Quanta Signs</title>
<link href="https://fonts.googleapis.com/css2?family=Open+Sans:wght@300;400;600;700&display=swap" rel="stylesheet">
<style>
:root{
  --yellow:#f2ad2c;
  --nav:#2a2a2a;
  --red:#c8161c;
  --orange:#f5940f;
  --blue:#1b2a8f;
  --ink:#222;
  --muted:#777;
  --page:#f3f3f3;
  --footer:#2f2f2f;
}
*{margin:0;padding:0;box-sizing:border-box}
html,body{width:1015px;height:1200px;overflow:hidden}
body{position:relative;font-family:'Open Sans',sans-serif;background:var(--page);color:var(--ink)}
.abs{position:absolute}
.header{left:0;top:0;width:1015px;height:72px;background:var(--yellow);border-bottom:2px solid #d8951e}
.brand{left:146px;top:20px;display:flex;align-items:center;gap:8px}
.brand-mark{width:22px;height:22px;background:var(--red)}
.brand-name{font-size:24px;font-weight:700;color:var(--red);letter-spacing:.5px}
.nav{left:450px;top:18px;width:421px;height:37px;background:var(--nav);border:1px solid #111;border-radius:2px;display:flex}
.nav a{flex:1;color:#fff;font-size:10px;font-weight:600;text-decoration:none;display:flex;align-items:center;justify-content:center;border-right:1px solid #444}
.nav a:last-child{border-right:0}
.hero{left:0;top:74px;width:1015px;height:438px;background:radial-gradient(ellipse at 50% 10%,#8a7b6a 0%,#4a4640 35%,#262626 75%,#1c1c1c 100%)}
.hero-photos{left:148px;top:46px;width:446px;height:330px;background:linear-gradient(160deg,#f4f4f4,#cfd3d8 60%,#9aa0a8);border:6px solid #fff;box-shadow:0 6px 14px rgba(0,0,0,.5)}
.dots{left:441px;top:390px;display:flex;gap:3px}
.dots span{width:7px;height:7px;border-radius:50%;background:#fff}
.dots span:first-child{background:var(--orange)}
.hero-text{left:644px;top:62px;width:210px;color:#fff}
.eyebrow{font-size:9px;font-weight:600}
.hero-title{font-size:25px;font-weight:600;margin:2px 0 14px;letter-spacing:.3px}
.hero-text p{font-size:11.5px;line-height:14.5px;margin-bottom:14px;font-weight:400}
.btn{background:var(--red);color:#fff;font-family:inherit;border:1px solid #9e0f13;display:inline-flex;align-items:center;justify-content:center}
.btn-read{left:643px;top:406px;width:77px;height:30px;font-size:14px;font-weight:300}
.btn-small{width:44px;height:20px;font-size:10px;top:751px}
h2{font-weight:400;font-size:19px;letter-spacing:-.3px;color:#222}
.thumb{top:576px;width:151px;height:150px;border:2px solid #e4e4e4;background:#ccc}
.caption{top:731px;width:151px;text-align:center;font-size:8.5px;color:#444}
.quote-tab{left:661px;top:545px;width:163px;height:31px;background:var(--orange);color:#fff;font-size:18px;font-weight:300;display:flex;align-items:center;justify-content:center}
.quote-box{left:656px;top:574px;width:216px;height:160px;background:#fff;border:1px solid #eaeaea;border-radius:3px;padding:14px 18px 0}
.quote-box label{display:block;font-size:9.5px;color:#333;margin-bottom:4px}
.field{width:180px;height:17px;border:1px solid #e2e2e2;margin-bottom:10px}
.field.area{height:46px}
.about-text{left:146px;top:862px;width:480px;font-size:9.5px;line-height:16px;color:var(--muted);font-weight:300}
.about-text p{margin-bottom:16px}
.services-panel{left:658px;top:820px;width:213px;height:300px;background:linear-gradient(90deg,#e9e9e9,#f3f3f3 12px)}
.services{left:680px;top:863px;width:190px;list-style:none}
.services li{height:37.5px;border-bottom:1px solid #e2e2e2;font-size:12px;color:var(--blue);display:flex;align-items:center;gap:8px;padding-bottom:4px}
.services li::before{content:"";width:5px;height:5px;border-radius:50%;background:var(--blue)}
.store{top:1026px;font-size:8.5px;line-height:11px;color:#666;font-weight:300}
.store h3{font-size:15px;color:var(--red);font-weight:600;line-height:16px}
.store .gap{margin-top:11px}
.store a{display:block;margin-top:6px;font-size:9.5px;color:var(--blue)}
.footer{left:0;top:1150px;width:1015px;height:50px;background:var(--footer);border-top:1px solid #444}
.footer-nav{left:144px;top:1171px;display:flex;gap:9px;font-size:8px;color:#ddd}
.copyright{right:144px;top:1171px;font-size:8px;color:#ddd}
</style>
</head>
<body>
<header class="abs header">
  <div class="abs brand"><span class="brand-mark"></span><span class="brand-name">Quanta Signs</span></div>
  <nav class="abs nav"><a>Home</a><a>About Us</a><a>Our Services</a><a>Our Portfolio</a><a>Contact Us</a></nav>
</header>

<section class="abs hero">
  <div class="abs hero-photos" role="img" aria-label="Stack of photos showing signwritten vehicles"></div>
  <div class="abs dots"><span></span><span></span><span></span></div>
  <div class="abs hero-text">
    <div class="eyebrow">WELCOME TO</div>
    <div class="hero-title">QUANTA SIGNS</div>
    <p>Le Lorem Ipsum est simplement du faux texte employé dans la composition et la mise en page avant impression.</p>
    <p>Le Lorem Ipsum est le faux texte standard de l'imprimerie depuis les années 1500, quand un peintre anonyme assembla.</p>
    <p>Ensemble des morceaux de texte pour réaliser un livre spécimen de polices de texte.</p>
  </div>
</section>
<span class="abs btn btn-read">Read More</span>

<h2 class="abs" style="left:146px;top:539px">Image Gallery</h2>
<div class="abs thumb" style="left:147px;background:linear-gradient(#c9c9c4,#d8c8a0)" role="img" aria-label="Red triangular road warning sign"></div>
<div class="abs thumb" style="left:314px;background:linear-gradient(#2a2a2a,#3a3020)" role="img" aria-label="Yellow construction hazard signs"></div>
<div class="abs thumb" style="left:480px;background:linear-gradient(#8ea0b4,#5a6a7c)" role="img" aria-label="Businessman holding a yellow road sign"></div>
<div class="abs caption" style="left:147px">Contrairement à une opinion</div>
<div class="abs caption" style="left:314px">Contrairement à une opinion</div>
<div class="abs caption" style="left:480px">Contrairement à une opinion</div>
<span class="abs btn btn-small" style="left:580px">Veiw All</span>

<div class="abs quote-tab">Online quote form</div>
<form class="abs quote-box">
  <label>Name :</label><div class="field"></div>
  <label>Email :</label><div class="field"></div>
  <label>Comments :</label><div class="field area"></div>
</form>
<span class="abs btn btn-small" style="left:827px">Submit</span>

<div class="abs services-panel"></div>
<h2 class="abs" style="left:146px;top:830px">About Us</h2>
<div class="abs about-text">
  <p>Quanta Signs is a Western Australian owned and managed company that was founded in 2005 and is fast becoming one of the state's leading manufacturer of quality signage.</p>
  <p>Supplying signage for any application. Vinyl Computer Cut Lettering, Large Format Digital Print, Photo quality, Banners, Roster signs, Pull up Displays, Vehicle and Shop Windows. From small stickers to large format just to name a few.</p>
</div>

<h2 class="abs" style="left:680px;top:830px">Services</h2>
<ul class="abs services">
  <li>Quality Stickers &amp; Decals</li>
  <li>All Sign Types</li>
  <li>Vehicle Signage</li>
  <li>Magnets</li>
  <li>Construction and safety Signs</li>
  <li>Window Signage</li>
  <li>Laminating</li>
</ul>

<h2 class="abs" style="left:146px;top:986px">Store Locations</h2>
<div class="abs store" style="left:147px"><h3>Eastbrook</h3>Unit 2, 18-22 Harbour Avenue<br>Eastbrook, WA 6100<div class="gap">Phone: (08) 5550 0101<br>Fax: (08) 5550 0102</div><a>View Map</a></div>
<div class="abs store" style="left:290px"><h3>Northgate</h3>Shop 7, 40 Bay Promenade,<br>Northgate,W.A<div class="gap">Phone: 08 5550 0188</div><a style="margin-top:17px">View Map</a></div>
<div class="abs store" style="left:430px"><h3>Eastbrook</h3>310 Lakeview Road<br>Lakeside, WA<div class="gap">Phone:08 5550 0142</div><a style="margin-top:17px">View Map</a></div>
<div class="abs store" style="left:542px"><h3>Westhaven</h3>310 Lakeview Road<br>Lakeside, WA<div class="gap">Phone:08 5550 0142</div><a style="margin-top:17px">View Map</a></div>

<footer class="abs footer"></footer>
<div class="abs footer-nav"><span>Home</span><span>About Us</span><span>Our Services</span><span>Our Portfolio</span><span>Contact Us</span></div>
<div class="abs copyright">© Copyrights 2013 All rights Reserved</div>
</body>
</html>
```